Dentist's Office needs desktop and mobile website design

This is a turnkey project where we are looking for a bright, elegant, modern website design, both for desktop and mobile. Our existing website is hosted on Google sites. We also require the new design to be set up and fully functional - both desktop and mobile - on Google sites. If Google sites is too limiting, its ok to use a platform like Wix or Squarespace. If using these, we will need you to point our domain to the new Wix site, and hand us the credentials so we can continue to update the site.

We want to continue using our current logo so the new website colors need to go with the logo. Our existing website can be found at www.smilebay47.com.

We want the new website to have the following pages:
1. Home - similar content to our current home page at http://www.smilebay47.com

We also have pictures of our office and team that we would like to show up on the home page in a collage, slide show, or some other creative. Pictures can be found here: https://files.exampleshare.net/folderview?id=7KQ2MVRAXPL4hYwnBzTcLdEgHsJu&usp=sharing

Not all pictures have to be used; use as many as needed.

In addition to the content on our current home page, we would like a small section for dental quotes where we could rotate quotes. Sample quotes can be found at http://www.sayingsmeadow.net/dental.html

If above content is too much to fit on one page, it is ok to split into two.

2. Our team - similar to http://www.smilebay47.com/our-dentist-1 . In addition, we want short bios and pictures of other staff added to this page. Pictures and bios can be found here: https://files.exampleshare.net/folderview?id=7KQ2MVRAXPL4hYwnBzTcLdEgHsJu&usp=sharing

3. Reviews - similar to http://www.smilebay47.com/patient-testimonials-1

4. Services - provide a summary of services we provide from http://www.smilebay47.com/dental-services . No need for detailed pages pages for each treatment we have on our current website.

5. Contact Us - http://www.smilebay47.com/contact-us

Target Market(s)

local population

Industry/Entity Type

Healthcare

Coding

Coded - Design and coding required

Number of Pages Required

5+ page

Font styles to use
Sans Serif

Requirements
Nice to have
• animated icons would be cool

```html
<!DOCTYPE html>
<html lang="en">
<head>
<meta charset="utf-8">
<title>Harborview Dental Care</title>
<link href="https://fonts.googleapis.com/css2?family=Roboto:wght@300;400;500;700;900&display=swap" rel="stylesheet">
<style>
:root{
  --orange:#dd812f;
  --orange-bright:#ec8a2e;
  --gold:#f7c21b;
  --page:#f4f4f4;
  --ink:#444;
  --muted:#666;
  --line:#e2e2e2;
  --white:#fff;
}
*{margin:0;padding:0;box-sizing:border-box}
html,body{width:884px;height:1200px;overflow:hidden}
body{background:var(--page);font-family:'Roboto',sans-serif;color:var(--ink);position:relative}
.abs{position:absolute}

.brand{left:352px;top:24px;width:180px;text-align:center;display:flex;align-items:center;justify-content:center;gap:8px;color:var(--orange);font-weight:300;font-size:25px;line-height:1.05}
.brand-dot{width:14px;height:14px;border-radius:50%;background:var(--orange);flex:none}
.contact{right:66px;top:28px;text-align:right;color:var(--muted)}
.contact .phone{font-size:20px;font-weight:300;letter-spacing:.3px}
.contact .addr{font-size:8.5px;line-height:11px}

.nav{left:112px;top:105px;display:flex;align-items:center;font-size:10.5px;color:#555}
.nav a{color:inherit;text-decoration:none}
.nav .sep{color:var(--orange);margin:0 9px}
.nav .active{background:var(--orange);color:var(--white);border-radius:13px;padding:6px 15px;margin-right:10px}

.hero{left:63px;top:139px;width:758px;height:224px;background:var(--orange);border-radius:12px;overflow:hidden;color:var(--white)}
.hero-title{position:absolute;left:356px;top:40px;font-weight:300;font-size:29px;line-height:32px}
.hero-title b{font-weight:900;font-size:36px}
.hero-title .l3{padding-left:58px;display:block;margin-top:-2px}
.hero-text{position:absolute;left:413px;top:136px;width:280px;font-size:11px;line-height:14px;font-weight:300}
.hero-text a{color:var(--gold);font-weight:500;text-decoration:underline}

.card{top:385px;width:239px;height:255px;background:var(--white);border:1px solid var(--line);border-radius:10px;overflow:hidden;text-align:center}
.card h2{position:absolute;left:25px;top:28px;text-align:left;font-weight:300;font-size:20px;line-height:22px;color:#555}
.card h2 span{color:var(--orange);display:flex;align-items:center;gap:6px}
.card .photo{position:absolute;left:0;top:84px;width:100%;height:72px}
.card p{position:absolute;left:15px;right:15px;font-size:8.5px;line-height:11px;color:#444}
.card .cta{font-size:8.5px}
.card-dentist .photo{top:0;height:162px;background:linear-gradient(90deg,#e6e6e6,#fafafa 60%,#e9e9e9)}
.portrait{position:absolute;left:55px;top:28px;width:124px;height:126px;border-radius:9px;border:2px solid #f5f5f5;background:linear-gradient(160deg,#f0a933,#d98d2a)}
.card-dentist h3{position:absolute;top:158px;width:100%;color:var(--orange);font-size:12px;font-weight:700}
.card-dentist a{color:var(--orange)}

.quote{left:150px;top:676px;width:584px;text-align:center}
.quote q{quotes:none;font-size:16.5px;font-weight:300;color:#555}
.quote cite{display:block;font-style:normal;font-weight:500;font-size:14px;color:#555;margin-top:4px}
.qmark{position:absolute;top:-4px;color:var(--orange);font-size:44px;font-weight:900;line-height:1}

.band{left:0;top:748px;width:884px;height:235px;background:var(--orange);color:var(--white)}
.band h2{position:absolute;top:32px;width:100%;text-align:center;font-weight:400;font-size:22px;letter-spacing:.5px}
.band .rule{position:absolute;top:46px;height:1px;background:rgba(255,255,255,.45)}
.review{position:absolute;top:92px;width:370px}
.review .avatar{position:absolute;left:0;top:0;width:80px;height:80px;border-radius:50%;background:#c9ccd0;border:2px solid rgba(255,255,255,.6)}
.review .body{position:absolute;left:98px;top:0;width:266px}
.review time{display:block;font-size:8.5px;font-weight:700;margin-bottom:8px}
.review p{font-size:10.5px;line-height:12.7px}
.review a{display:block;margin-top:6px;color:var(--gold);font-size:10.5px;text-decoration:none}

.members h2{position:absolute;top:1004px;width:884px;text-align:center;font-size:16px;font-weight:300;color:#555}
.badge{position:absolute;top:1036px;text-align:center;font-size:10px;color:#777}
.badge .shape{margin:0 auto 18px;background:#cfd3d6;border-radius:4px}
.vline{position:absolute;top:1034px;width:1px;height:75px;background:#ccc}

.footer-rule{left:64px;top:1154px;width:757px;height:1px;background:#ccc}
.footer{left:64px;top:1163px;font-size:10px;color:#777}
.footer .sep{color:var(--orange);margin:0 5px}
</style>
</head>
<body>

<div class="abs brand"><span class="brand-dot"></span><span>Harborview<br>Dental Care</span></div>
<div class="abs contact">
  <div class="phone">555-014-2298</div>
  <div class="addr">4820 Willow Crest Ave, Lindale, CA 95000<br>(next to Sunrise Market)</div>
</div>

<nav class="abs nav">
  <a class="active" href="#">Home</a>
  <a href="#">Meet Our Dentist</a><span class="sep">|</span>
  <a href="#">Patient Testimonials</a><span class="sep">|</span>
  <a href="#">Dental Services</a><span class="sep">|</span>
  <a href="#">Insurance Plans</a><span class="sep">|</span>
  <a href="#">Financing</a><span class="sep">|</span>
  <a href="#">Specials</a><span class="sep">|</span>
  <a href="#">Contact Us</a>
</nav>

<section class="abs hero">
  <h1 class="hero-title">It's our <b>genuine care</b> &amp;<br><b>gentle nature</b><span class="l3">that sets us apart!</span></h1>
  <p class="hero-text">We want to provide you with everything you could want in a dental office: excellent work, a gentle nature, and a friendly staff - all in a comfortable location and at a great price. <a href="#">more...</a></p>
</section>

<article class="abs card" style="left:64px">
  <h2>Weekend &amp; Emergency<span>Appointments
    <svg width="20" height="20" viewBox="0 0 20 20" fill="none" stroke="#dd812f" stroke-width="1.6"><rect x="2" y="4" width="13" height="12" rx="1"/><path d="M2 8h13M5 2v4M12 2v4"/><circle cx="15" cy="15" r="4" fill="#fff"/><path d="M15 13v2h1.5"/></svg></span></h2>
  <div class="photo" role="img" aria-label="Photo of a dental consultation at a desk" style="background:linear-gradient(90deg,#d8cfe0,#e9eef4 40%,#c9d8e6)"></div>
  <p style="top:178px">Weekend &amp; Emergency Appointments</p>
  <p class="cta" style="top:220px">click for office hours</p>
</article>

<article class="abs card" style="left:322px">
  <h2>New Patient<span>Specials
    <svg width="14" height="14" viewBox="0 0 24 24" fill="#dd812f"><path d="M12 2l3 7 7 .6-5.3 4.7 1.6 7.3L12 17.8 5.7 21.6l1.6-7.3L2 9.6 9 9z"/></svg></span></h2>
  <div class="photo" role="img" aria-label="Photo of a smiling patient in a dental chair" style="background:linear-gradient(90deg,#2f5fa8,#e8c6b0 35%,#f1e6e0 65%,#8a8f96)"></div>
  <p style="top:178px">Free exam and consultation for non-insured patients!<br>Free teeth whitening for insured patients!<br>(PPO only)</p>
  <p class="cta" style="top:221px">click to print coupons</p>
</article>

<article class="abs card card-dentist" style="left:581px">
  <div class="photo" role="img" aria-label="Stethoscope backdrop"></div>
  <div class="portrait" role="img" aria-label="Portrait of the dentist"></div>
  <h3>Dr Meera Sandhu</h3>
  <p style="top:178px">Our dentist, Dr Meera Sandhu, is all about passion and compassion! Passion for dentistry and compassion for the patients is what you will experience when you visit the office extra mile to ensure that. <a href="#">more...</a></p>
</article>

<blockquote class="abs quote">
  <span class="qmark" style="left:5px">“</span>
  <q>A dentist at work in his vocation always looks down in the mouth.</q>
  <cite>Harold T. Wexley</cite>
  <span class="qmark" style="right:5px">”</span>
</blockquote>

<section class="abs band">
  <span class="rule" style="left:64px;width:258px"></span>
  <h2>TESTIMONIALS</h2>
  <span class="rule" style="left:512px;width:309px"></span>
  <div class="review" style="left:68px">
    <div class="avatar" role="img" aria-label="Photo of a male patient"></div>
    <div class="body">
      <time>7 December 2014</time>
      <p>... I've always been afraid of the dentist because of past dental work. But a friend of my husband referred us to Harborview Dental Care and it changed my life. I wouldn't smile before. Now you cant get me to stop smiling. The work was painless...</p>
      <a href="#">+ read more</a>
    </div>
  </div>
  <div class="review" style="left:463px">
    <div class="avatar" role="img" aria-label="Photo of a female patient"></div>
    <div class="body">
      <time style="padding-left:5px">8 June 2014</time>
      <p>Dummy text to be replaced here, dummy text to be replaced here, dummy text to be replaced here.here, dummy text to be replaced here, dummy text to be replaced here.here, dummy text to be replaced here, dummy text to be replaced here.here,</p>
      <a href="#" style="padding-left:5px">+ read more</a>
    </div>
  </div>
</section>

<section class="members">
  <h2>Member of:</h2>
  <div class="badge" style="left:166px;width:136px"><div class="shape" style="width:134px;height:40px" role="img" aria-label="Association badge"></div>National Dental Guild</div>
  <span class="vline" style="left:340px"></span>
  <div class="badge" style="left:370px;width:140px"><div class="shape" style="width:84px;height:60px;margin-bottom:0" role="img" aria-label="Association badge"></div></div>
  <div class="badge" style="left:366px;top:1108px;width:148px">State Dental Alliance</div>
  <span class="vline" style="left:542px"></span>
  <div class="badge" style="left:562px;width:138px"><div class="shape" style="width:82px;height:50px;margin-bottom:22px" role="img" aria-label="Society badge"></div>Valley Dental Society</div>
</section>

<div class="abs footer-rule"></div>
<footer class="abs footer">Sign in<span class="sep">|</span>Recent Site Activity<span class="sep">|</span>Report Abuse<span class="sep">|</span>Print Page</footer>

</body>
</html>
```